Website for an electrical contractor :)

We are after a web site which can show pictures of our jobs and our capability in a professional, creative and easily understood way.

----- Brightmoor Electrical ------

We really want a visually good looking website with three sections

Section one:
'Completed projects'
We have a few pictures of jobs which we've completed and would like to show off with a brief description. (see uploads)

Section two:
'Our capabilities'
Just a list of what services we offer

Section three:
We would like a 'contact us' section which people can send us a short msg and upload a file for plans to be able to send to us. We would need their name, phone number and email details. We would also need a short privacy policy saying 'we do not disclose information to third parties'.
We also want to display our contact number and postal address

Good luck :)

Target Market(s)

Adults 25 years+
Business owners
Builders
Real estate agents

Industry/Entity Type

Electrical

Colors

Designer to choose colors to be used in the design.

Requirements
Must have
• Visually appealing
Easy to understand
In the 'Completed projects' section, must have a list for each project we do i can upload pictures for it.

```html
<!DOCTYPE html>
<html lang="en">
<head>
<meta charset="utf-8">
<title>Brightmoor Electrical</title>
<link href="https://fonts.googleapis.com/css2?family=Roboto:wght@300;400;500;700&family=Ubuntu:wght@500&display=swap" rel="stylesheet">
<style>
:root{
  --red:#e21d24;
  --ink:#333;
  --text:#555;
  --muted:#8a8a8a;
  --line:#dcdcdc;
  --tab-dark:#585858;
  --footer:#5b5b5b;
  --footer-line:#777;
  --field:#f1f1f1;
  --white:#fff;
}
*{box-sizing:border-box;margin:0;padding:0}
html,body{width:705px;height:1200px;overflow:hidden;background:var(--white)}
body{position:relative;font-family:"Roboto",sans-serif;color:var(--text)}
.abs{position:absolute}

/* header */
.site-header{position:absolute;left:0;top:0;width:705px;height:71px;border-top:3px solid #555;background:var(--white)}
.brand{position:absolute;left:79px;top:14px;display:flex;align-items:center;gap:10px}
.brand-dot{width:14px;height:14px;border-radius:50%;background:var(--red)}
.brand-name{font-family:"Roboto",sans-serif;font-weight:400;font-size:31px;color:#555;letter-spacing:-.5px}
.social{position:absolute;top:10px;left:549px;display:flex;gap:7px}
.social span{width:22px;height:22px;background:#2f6fb3;display:block}
.header-contact{position:absolute;top:40px;left:398px;display:flex;gap:26px;font-size:10.5px;color:#444;align-items:center}
.header-contact div{display:flex;align-items:center;gap:6px}

/* hero */
.hero{position:absolute;left:0;top:71px;width:705px;height:274px;background:linear-gradient(180deg,#8d8f8f 0%,#d7d9d9 30%,#b4b6b6 55%,#4b4c4e 100%)}
.hero-arrow{position:absolute;top:125px;width:22px;height:22px;border-radius:50%;background:rgba(255,255,255,.9);display:flex;align-items:center;justify-content:center}
.hero-title{position:absolute;left:0;right:0;top:218px;text-align:center;font-family:"Ubuntu",sans-serif;font-weight:500;font-size:16.5px;line-height:22px;color:var(--white)}

/* about */
.about-title{position:absolute;left:0;right:0;top:356px;text-align:center;font-size:18px;color:var(--red);font-weight:300}
.about-title b{font-weight:400;color:#555;font-size:22px;margin-left:6px}
.about-text{position:absolute;left:87px;width:531px;top:393px;text-align:center;font-size:8.6px;line-height:14px;color:#444}
.rule{position:absolute;left:79px;width:548px;height:1px;background:var(--line)}

/* capability */
.section-title{position:absolute;left:0;right:0;text-align:center;font-size:17.5px;color:#333}
.section-title em{font-style:normal;color:var(--red)}
.cap-panel{position:absolute;left:79px;top:511px;width:548px;height:243px;border:1px solid var(--line)}
.tab{position:absolute;top:-1px;height:25px;width:275px;color:var(--white);font-size:14px;text-align:center;line-height:25px}
.tab-res{left:-1px;background:var(--red)}
.tab-res::after{content:"";position:absolute;left:129px;bottom:-6px;border:6px solid transparent;border-bottom:0;border-top-color:var(--red)}
.tab-com{left:274px;width:274px;background:var(--tab-dark)}
.cap-list{position:absolute;top:35px;list-style:none;font-size:9.3px;color:#333}
.cap-list li{height:17.6px;display:flex;align-items:center;gap:9px}
.cap-list svg{flex:none}

/* gallery */
.gallery{position:absolute;left:79px;top:767px;width:548px;height:148px;border:1px solid var(--line);box-shadow:0 3px 5px rgba(0,0,0,.08)}
.gallery-title{position:absolute;left:7px;top:9px;font-size:15.5px;color:#333}
.gallery-line{position:absolute;left:126px;top:19px;width:334px;height:1px;background:var(--red)}
.gallery-line::before,.gallery-line::after{content:"";position:absolute;top:-3px;width:6px;height:6px;background:var(--red);transform:rotate(45deg)}
.gallery-line::before{left:-3px}.gallery-line::after{right:-3px}
.gallery-nav{position:absolute;left:476px;top:13px;display:flex;gap:5px}
.view-all{position:absolute;left:498px;top:12px;width:44px;height:17px;background:var(--red);color:var(--white);font-size:8.5px;text-align:center;line-height:17px}
.project-card{position:absolute;top:38px;width:121px;height:101px;border:1px solid #ddd;padding:2px;background:var(--white)}
.project-photo{height:61px;width:100%}
.project-card h3{font-size:8.6px;font-weight:700;color:#222;margin:5px 0 1px 2px}
.project-card p{font-size:8px;line-height:11px;color:#444;margin-left:2px}

/* form */
.form-title{position:absolute;left:79px;top:938px;font-size:17.5px;color:#333}
.form-title em{font-style:normal;color:var(--red)}
.field{position:absolute;left:79px;width:269px;height:22px;background:var(--field);border:1px solid #e2e2e2;font-size:8.6px;color:#444;padding:6px 9px}
.field-message{left:359px;top:982px;width:268px;height:88px;padding:7px 21px}
.send-btn{position:absolute;left:557px;top:1081px;width:71px;height:23px;background:var(--red);color:var(--white);border-radius:3px;font-weight:700;font-size:12px;text-align:center;line-height:23px}

/* footer */
.site-footer{position:absolute;left:0;top:1117px;width:705px;height:83px;background:var(--footer);color:var(--white);font-size:8px}
.footer-label{position:absolute;left:79px;top:14px;font-weight:700;font-size:10px}
.footer-item{position:absolute;top:15px;display:flex;gap:6px;line-height:11px}
.footer-sep{position:absolute;top:15px;width:1px;height:20px;background:var(--footer-line)}
.footer-rule{position:absolute;left:79px;top:50px;width:548px;height:1px;background:var(--footer-line)}
.copyright{position:absolute;left:82px;top:60px;font-size:7.6px}
.disclaimer{position:absolute;left:415px;top:58px;font-size:7.6px}
.disclaimer b{font-size:10px;margin-right:4px}
</style>
</head>
<body>

<header class="site-header">
  <div class="brand"><span class="brand-dot"></span><span class="brand-name">Brightmoor</span></div>
  <div class="social" aria-label="Social links"><span></span><span style="background:#2aa3df"></span><span style="background:#1f6fa8"></span></div>
  <div class="header-contact">
    <div><svg width="7" height="10" viewBox="0 0 7 10"><path d="M1 0h2l1 3-1.5 1a5 5 0 0 0 2 3L6 6l1 2v1.5C5 10 0 6 0 1z" fill="#555"/></svg>555-018-2244</div>
    <div><svg width="11" height="8" viewBox="0 0 11 8"><rect width="11" height="8" fill="#555"/><path d="M0 0l5.5 4L11 0" stroke="#fff" fill="none"/></svg>info@brightmoorelectrical.com</div>
  </div>
</header>

<section class="hero" role="img" aria-label="Photo of an empty, bright office floor with windows along the walls">
  <div class="hero-arrow" style="left:62px"><svg width="8" height="8" viewBox="0 0 8 8"><path d="M6 0L2 4l4 4z" fill="#333"/></svg></div>
  <div class="hero-arrow" style="left:619px"><svg width="8" height="8" viewBox="0 0 8 8"><path d="M2 0l4 4-4 4z" fill="#333"/></svg></div>
  <h1 class="hero-title">We are in Electrical &amp; communication Industry Supply Service<br>to Residential &amp; Commerical Industry</h1>
</section>

<h2 class="about-title">About<b>Brightmoor</b></h2>
<p class="about-text">Lorem ipsum dolor sit amet, consectetuer adipiscing elit,Sed diam nonummy nibh euismod tincidunt ut laoreet dolore magna aliquamerer erat volutpat. Ut wisi enim ad minim veniam, quis nostrud exerci tation ullamcorper suscipit lobortis nisl ut aliquip commodo consequat. Duis autem vel eum iriure dolor in hendrerit in vulputate velit esse molestie consequat, vel illum dolore eu feugiat nulla facilisis at vero eros et accumsan et iusto odio dignissim qui blandit praesent luptatumdeelenit augue duis dolore te feugait nulla facilisis.</p>
<div class="rule" style="top:472px"></div>

<h2 class="section-title" style="top:480px"><em>Our</em> Capability</h2>
<section class="cap-panel">
  <div class="tab tab-res">Residential</div>
  <div class="tab tab-com">Commercial / Industrial</div>
  <ul class="cap-list" style="left:70px">
    <li><svg width="8" height="8"><path d="M0 0l8 4-8 4 3-4z" fill="#777"/></svg>24hr Support / faults</li>
    <li><svg width="8" height="8"><path d="M0 0l8 4-8 4 3-4z" fill="#777"/></svg>RCD (Safety Switch) installations</li>
    <li><svg width="8" height="8"><path d="M0 0l8 4-8 4 3-4z" fill="#777"/></svg>Smoke alarms</li>
    <li><svg width="8" height="8"><path d="M0 0l8 4-8 4 3-4z" fill="#777"/></svg>Power points</li>
    <li><svg width="8" height="8"><path d="M0 0l8 4-8 4 3-4z" fill="#777"/></svg>Lighting points</li>
    <li><svg width="8" height="8"><path d="M0 0l8 4-8 4 3-4z" fill="#777"/></svg>External lighting</li>
    <li><svg width="8" height="8"><path d="M0 0l8 4-8 4 3-4z" fill="#777"/></svg>Sensor lighting</li>
    <li><svg width="8" height="8"><path d="M0 0l8 4-8 4 3-4z" fill="#777"/></svg>Switching</li>
    <li><svg width="8" height="8"><path d="M0 0l8 4-8 4 3-4z" fill="#777"/></svg>Antennas and Arial points</li>
    <li><svg width="8" height="8"><path d="M0 0l8 4-8 4 3-4z" fill="#777"/></svg>Dimmers</li>
    <li><svg width="8" height="8"><path d="M0 0l8 4-8 4 3-4z" fill="#777"/></svg>Ceiling fans</li>
  </ul>
  <ul class="cap-list" style="left:312px">
    <li><svg width="8" height="8"><path d="M0 0l8 4-8 4 3-4z" fill="#777"/></svg>Exhaust fans</li>
    <li><svg width="8" height="8"><path d="M0 0l8 4-8 4 3-4z" fill="#777"/></svg>Kitchen / Bathroom Projects</li>
    <li><svg width="8" height="8"><path d="M0 0l8 4-8 4 3-4z" fill="#777"/></svg>Re-wires</li>
    <li><svg width="8" height="8"><path d="M0 0l8 4-8 4 3-4z" fill="#777"/></svg>Smart wiring</li>
    <li><svg width="8" height="8"><path d="M0 0l8 4-8 4 3-4z" fill="#777"/></svg>Phone points</li>
    <li><svg width="8" height="8"><path d="M0 0l8 4-8 4 3-4z" fill="#777"/></svg>Data points</li>
    <li><svg width="8" height="8"><path d="M0 0l8 4-8 4 3-4z" fill="#777"/></svg>Mains/sub mains cabling</li>
    <li><svg width="8" height="8"><path d="M0 0l8 4-8 4 3-4z" fill="#777"/></svg>Switchboard installations/relocations</li>
    <li><svg width="8" height="8"><path d="M0 0l8 4-8 4 3-4z" fill="#777"/></svg>Compliance investigations/inspections</li>
    <li><svg width="8" height="8"><path d="M0 0l8 4-8 4 3-4z" fill="#777"/></svg>Concrete and wall chasing</li>
    <li><svg width="8" height="8"><path d="M0 0l8 4-8 4 3-4z" fill="#777"/></svg>Temporary builders site power</li>
  </ul>
</section>

<section class="gallery">
  <h2 class="gallery-title">Projects Gallery</h2>
  <div class="gallery-line"></div>
  <div class="gallery-nav">
    <svg width="6" height="9"><path d="M5 0L1 4.5 5 9" stroke="#e21d24" stroke-width="1.6" fill="none"/></svg>
    <svg width="6" height="9"><path d="M1 0l4 4.5L1 9" stroke="#e21d24" stroke-width="1.6" fill="none"/></svg>
  </div>
  <div class="view-all">View All</div>
  <article class="project-card" style="left:7px">
    <div class="project-photo" role="img" aria-label="Photo of a finished outdoor courtyard with garden lighting" style="background:linear-gradient(180deg,#8e9296,#5d5b55 60%,#3b3a36)"></div>
    <h3>Lorem ipsum dolor sit</h3><p>Lorem ipsum dolor sit amet, tuer adipiscing elit,Sed</p>
  </article>
  <article class="project-card" style="left:144px">
    <div class="project-photo" role="img" aria-label="Photo of a completed kitchen fit-out with lighting" style="background:linear-gradient(180deg,#5a4b3c,#b29a7e 55%,#d8d2c6)"></div>
    <h3>Lorem ipsum dolor sit</h3><p>Lorem ipsum dolor sit amet, tuer adipiscing elit,Sed</p>
  </article>
  <article class="project-card" style="left:282px">
    <div class="project-photo" role="img" aria-label="Photo of a switchboard installation with wiring" style="background:linear-gradient(90deg,#6e3a2c,#b8755a 40%,#7a4536 70%,#a0604a)"></div>
    <h3>Lorem ipsum dolor sit</h3><p>Lorem ipsum dolor sit amet, tuer adipiscing elit,Sed</p>
  </article>
  <article class="project-card" style="left:419px">
    <div class="project-photo" role="img" aria-label="Photo of conduit laid out on a slab before concrete pour" style="background:linear-gradient(160deg,#6b5f53,#9b8f82 50%,#5d544b)"></div>
    <h3>Lorem ipsum dolor sit</h3><p>Lorem ipsum dolor sit amet, tuer adipiscing elit,Sed</p>
  </article>
</section>

<h2 class="form-title"><em>Fill In The Form</em> And We’ll Be In Touch…</h2>
<div class="rule" style="top:966px"></div>
<form>
  <div class="field" style="top:983px">First name:</div>
  <div class="field" style="top:1016px">Last Name:</div>
  <div class="field" style="top:1048px">Email:</div>
  <div class="field" style="top:1081px">Contact phone:</div>
  <div class="field field-message">Message:</div>
  <div class="send-btn">SEND</div>
</form>

<footer class="site-footer">
  <div class="footer-label">Contact Detail:</div>
  <div class="footer-item" style="left:162px"><svg width="6" height="9"><path d="M3 9L0 3a3 3 0 0 1 6 0z" fill="#ddd"/><circle cx="3" cy="3" r="1" fill="#5b5b5b"/></svg><span>P.O Box 417 Harbour Vale W.A 6107<br>A.B.N: 48 612 390 275</span></div>
  <div class="footer-sep" style="left:312px"></div>
  <div class="footer-item" style="left:326px"><svg width="6" height="9" viewBox="0 0 7 10"><path d="M1 0h2l1 3-1.5 1a5 5 0 0 0 2 3L6 6l1 2v1.5C5 10 0 6 0 1z" fill="#ddd"/></svg>0400 555 128</div>
  <div class="footer-sep" style="left:397px"></div>
  <div class="footer-item" style="left:409px"><svg width="9" height="7"><rect width="9" height="7" fill="#ddd"/><path d="M0 0l4.5 3.5L9 0" stroke="#5b5b5b" fill="none"/></svg>hello@brightmoorelectrical.com.au</div>
  <div class="footer-sep" style="left:543px"></div>
  <div class="footer-item" style="left:555px"><svg width="10" height="8"><rect x="1" y="3" width="8" height="5" fill="#ddd"/><path d="M0 3q5-4 10 0" stroke="#ddd" fill="none"/></svg>08 5550 3391</div>
  <div class="footer-rule"></div>
  <div class="copyright">Copyright 2015 Brightmoor Electrical. All rights reserved.</div>
  <div class="disclaimer"><b>Disclaimer:</b>we do not disclose information to third parties.</div>
</footer>

</body>
</html>
```